Web Design Project

We need a web design for a new business in Orland Park, IL.
We are a restaurant meal delivery business. We deliver from a variety of restaurants. We gives our customers an alternative to just pizza delivery.

Websites we like:
http://www.brambleporter.example/
https://www.quillfetchgo.example/Default.asp
www.wendlerunner.example/

Our current website is www.tovenbasket.example(not to be used as a guide, i'm looking for an original design)
Updates

Please no pictures of anything associated with Pizza.  We are a restaurant delivery business that gives our customers an alternative to just pizza delivery. 

This is my original logo.  I uploaded the file to the job brief and updated the brief some.

Target Market(s)

Two income households with children.

Industry/Entity Type

Business

Requirements
Must have
• Order Now button,and sliding photographs of food.
Nice to have
• a background other than white(it can be white if it works with the design)
Should not have
• A picture of pizza that cant be changed. It is ok if the photo is apart of sliding photo's, but pizza cant be the main focus of our delivery service.

```html
<!DOCTYPE html>
<html lang="en">
<head>
<meta charset="utf-8">
<title>Toven Basket – Restaurant Delivery</title>
<link href="https://fonts.googleapis.com/css2?family=Changa+One:ital@0;1&family=Open+Sans:ital,wght@0,400;0,600;1,700&family=PT+Sans+Narrow:wght@400;700&family=Yanone+Kaffeesatz:wght@500;700&display=swap" rel="stylesheet">
<style>
:root{
  --gold:#c99a48;
  --gold-light:#efcf6a;
  --gold-deep:#b68a3f;
  --red:#b8191f;
  --red-dark:#8e1116;
  --ink:#111;
  --dark:#1b1b1b;
  --footer-text:#e8e8e8;
  --muted:#9a9a9a;
  --white:#fff;
}
*{box-sizing:border-box;margin:0;padding:0}
html,body{width:1200px;height:1022px;overflow:hidden}
body{position:relative;font-family:"Open Sans",sans-serif;background:var(--dark);color:var(--ink)}
.hero{position:absolute;left:0;top:0;width:1200px;height:726px;
  background:radial-gradient(ellipse 520px 360px at 230px 120px,var(--gold-light),var(--gold) 70%,var(--gold-deep));
  border-top:3px solid #222}
.brand{position:absolute;left:150px;top:95px;display:flex;align-items:center;gap:10px}
.brand-mark{width:26px;height:26px;border-radius:50%;background:var(--red)}
.brand-name{font-family:"Open Sans",sans-serif;font-weight:600;font-size:30px;color:var(--red)}
.phone{position:absolute;left:478px;top:20px;display:flex;align-items:center;gap:6px}
.phone-number{font-family:"Yanone Kaffeesatz",sans-serif;font-weight:700;font-size:40px;color:var(--ink);margin-top:4px}
.login input{position:absolute;top:38px;width:163px;height:23px;border:1px solid #bbb;background:#f4f4f4;font:12px "Open Sans",sans-serif;padding-left:7px;color:#999}
.remember{position:absolute;left:996px;top:72px;font-size:12px;color:var(--white);display:flex;align-items:center;gap:4px;letter-spacing:.3px}
.remember span.box{width:11px;height:11px;background:#fff;border:1px solid #557}
.create{position:absolute;left:896px;top:106px;font-size:12px;color:var(--white);text-decoration:underline}
.signin{position:absolute;left:1023px;top:99px;width:74px;height:27px;border-radius:4px;background:linear-gradient(#444,#0b0b0b);color:#fff;font-size:15px;text-align:center;line-height:26px;border:1px solid #000}
.nav{position:absolute;left:438px;top:158px;display:flex;align-items:center;font-family:"PT Sans Narrow",sans-serif;font-weight:700;font-size:18px}
.nav a{color:#2a1a08;text-decoration:none;padding:0 19px;border-left:1px solid #a97b31;line-height:16px}
.nav a:nth-child(2){border-left:none}
.nav a.active{background:var(--red);color:#fff;border-radius:4px;padding:5px 9px;line-height:20px;border:1px solid #e16;margin-right:6px}
.order-intro{position:absolute;left:132px;top:244px}
.order-title{font-family:"Changa One",sans-serif;font-style:italic;font-size:40px;color:var(--red)}
.order-sub{font-family:"Open Sans",sans-serif;font-style:italic;font-weight:700;font-size:22px;line-height:28px;margin-top:2px;margin-left:2px}
.field-label{position:absolute;left:137px;font-size:14px;color:#fff}
.field{position:absolute;left:136px;width:228px;height:29px;background:#fff;border:1px solid #a88;border-radius:5px}
.select-caret{position:absolute;right:6px;top:6px;width:15px;height:15px;border:1px solid #666;background:#eee}
.order-btn{position:absolute;left:132px;top:534px;width:266px;height:68px;border-radius:16px;
  background:linear-gradient(#e2464a,#b8191f 55%,#8e1116);box-shadow:0 6px 8px rgba(0,0,0,.3);
  color:#fff;font-family:"Open Sans",sans-serif;font-weight:700;font-size:32px;letter-spacing:-.5px;line-height:68px;padding-left:26px}
.order-tag{position:absolute;left:352px;top:530px;width:52px;height:14px;background:#3a6f9a;transform:rotate(38deg);transform-origin:left top}
.slider{position:absolute;left:466px;top:241px;width:632px;height:366px;background:#fff;padding:10px;box-shadow:0 40px 40px -30px rgba(0,0,0,.45)}
.slide{position:relative;width:611px;height:346px;background:radial-gradient(ellipse at 60% 55%,#c8402a,#8a5a2a 45%,#3a2a1a 90%)}
.caption{position:absolute;left:0;top:25px;width:520px;background:rgba(0,0,0,.45);color:#fff;font-size:23px;line-height:32px;padding:2px 15px 3px}
.slide-bar{position:absolute;left:0;bottom:0;width:100%;height:36px;background:rgba(0,0,0,.65)}
.arrows{position:absolute;left:10px;top:8px;display:flex;gap:14px}
.dots{position:absolute;right:16px;top:9px;display:flex;gap:7px}
.dots span{width:16px;height:16px;border-radius:50%;background:var(--red)}
.dots span.on{background:#d4a34a}
.partners{position:absolute;left:128px;top:686px;width:968px;height:83px;background:#fff;border:3px solid #dba53f;border-radius:22px;display:flex;align-items:center}
.partners .nav-arrow{width:48px;display:flex;justify-content:center}
.partner-list{flex:1;display:flex;justify-content:space-between;align-items:center;padding:0 6px;font-family:"Open Sans",sans-serif;font-weight:600;font-size:14px;color:var(--red)}
.footer-cols{position:absolute;top:808px;left:0;width:1200px}
.col{position:absolute;top:0}
.col h3{font-family:"Changa One",sans-serif;font-style:italic;font-weight:400;font-size:23px;color:#c11a1f}
.col ul{list-style:none;margin-top:8px}
.col li{font-size:12.5px;color:var(--footer-text);line-height:20px}
.divider{position:absolute;top:822px;width:1px;height:130px;background:#444}
.footer-brand{position:absolute;left:900px;top:860px;display:flex;align-items:center;gap:8px;color:#8a8a8a;font-weight:600;font-size:24px}
.footer-brand .brand-mark{background:#777;width:22px;height:22px}
.bottom{position:absolute;left:0;top:975px;width:1200px;height:47px;background:#000;border-left:2px solid #b98a3f}
.bottom-links{position:absolute;left:113px;top:4px;font-size:11.5px;color:var(--muted);line-height:20px}
.bottom-links span{padding:0 5px}
.social{position:absolute;left:866px;top:7px;display:flex;gap:11px}
.social span{width:28px;height:28px}
</style>
</head>
<body>
<header class="hero">
  <div class="brand"><span class="brand-mark"></span><span class="brand-name">Toven Basket</span></div>

  <div class="phone">
    <svg width="58" height="68" viewBox="0 0 58 68" aria-hidden="true">
      <ellipse cx="32" cy="64" rx="24" ry="3" fill="rgba(0,0,0,.35)"/>
      <path d="M12 2 C4 6 0 18 4 32 C9 48 22 60 34 62 C40 63 44 58 46 54 L38 44 C35 46 31 48 28 45 C22 38 17 28 17 22 C17 18 21 16 24 14 L18 2 Z" fill="var(--red)"/>
    </svg>
    <span class="phone-number">555-014-3000</span>
  </div>

  <div class="login">
    <input style="left:757px" value="Email" aria-label="Email">
    <input style="left:935px" value="Password" aria-label="Password">
  </div>
  <div class="remember"><span class="box"></span>Remember me</div>
  <a class="create">Create an Account</a>
  <div class="signin">Sign In</div>

  <nav class="nav">
    <a class="active">Restaurants</a>
    <a>How Do I Order?</a>
    <a>Corporate</a>
    <a>Gift Certificate</a>
    <a>About Us</a>
    <a>Contact Us</a>
  </nav>

  <div class="order-intro">
    <div class="order-title">Ready to Order?</div>
    <p class="order-sub">Choose your favorite<br>restaurant below or select<br>your ZIP code.</p>
  </div>
  <div class="field-label" style="top:402px">Select Your ZIP Code</div>
  <div class="field" style="top:422px"><span class="select-caret"></span></div>
  <div class="field-label" style="top:463px">Search For Your ZIP Code</div>
  <div class="field" style="top:482px"></div>
  <div class="order-btn">ORDER NOW</div>
  <div class="order-tag"></div>

  <div class="slider">
    <div class="slide" role="img" aria-label="Photo of stir-fried meat and vegetables over rice on a red plate">
      <p class="caption">We make your life easier by delivering quality restaurant food to your home, office or hotel.</p>
      <div class="slide-bar">
        <div class="arrows">
          <svg width="12" height="20" viewBox="0 0 12 20"><path d="M9 2 L3 10 L9 18" stroke="#ddd" stroke-width="3" fill="none"/></svg>
          <svg width="12" height="20" viewBox="0 0 12 20"><path d="M3 2 L9 10 L3 18" stroke="#ddd" stroke-width="3" fill="none"/></svg>
        </div>
        <div class="dots"><span></span><span class="on"></span><span></span><span></span></div>
      </div>
    </div>
  </div>

  <div class="partners">
    <div class="nav-arrow"><svg width="16" height="30" viewBox="0 0 16 30"><path d="M13 2 L3 15 L13 28" stroke="#111" stroke-width="4" fill="none"/></svg></div>
    <div class="partner-list">
      <span>Lindo Pasta</span><span>Crumbline</span><span>Jade Pan</span><span>Crust Harbor</span><span>Oven Row</span><span>Hollow Oak</span><span>Kiln Street</span><span>Toastwell</span>
    </div>
    <div class="nav-arrow"><svg width="16" height="30" viewBox="0 0 16 30"><path d="M3 2 L13 15 L3 28" stroke="#111" stroke-width="4" fill="none"/></svg></div>
  </div>
</header>

<section class="footer-cols">
  <div class="col" style="left:144px"><h3>How Do Work</h3>
    <ul><li>Lorem ipsum dolor sit</li><li>Amet consectetuer</li><li>Adipiscing elit</li><li>Praesent vestibulum</li><li>Molestie lacus aenean</li></ul></div>
  <div class="col" style="left:403px"><h3>How Do i Order</h3>
    <ul><li>Lorem ipsum dolor sit</li><li>Amet consectetuer</li><li>Adipiscing elit</li><li>Praesent vestibulum</li><li>Molestie lacus aenean</li></ul></div>
  <div class="col" style="left:652px"><h3>Contact Us</h3>
    <ul><li>contact@tovenbasket.example</li><li>Phone:&nbsp; 555-014-3000</li><li>Fax: 555-014-0213</li><li>4410 W Marrow Lane Suite 12</li><li>Brackett Falls, IL 60999</li></ul></div>
</section>
<div class="divider" style="left:348px"></div>
<div class="divider" style="left:599px"></div>
<div class="footer-brand"><span class="brand-mark"></span><span>Toven Basket</span></div>

<footer class="bottom">
  <div class="bottom-links">
    Home<span>|</span>Restaurants<span>|</span>How Do I Order?<span>|</span>Corporate Account Signup<span>|</span>Gift Certificate<span>|</span>About Us<span>|</span>Comments<br>
    © 2013 Tovenbasket.<span></span>FAQ<span>|</span>Privacy Policy<span>|</span>Site Map.
  </div>
  <div class="social">
    <span style="background:#2d6fb4"></span><span style="background:#ccc"></span><span style="background:#3a8fb0"></span><span style="background:#4fb3e0"></span><span style="background:#1f6fa8"></span><span style="background:#d9321f"></span>
  </div>
</footer>
</body>
</html>
```